Need simple and modern looking business card with all my information on one side and logo on the other side
Info :
Company name - VELMAR CONSTRUCTION LLC
Company addres- 418 harbor 87th. Dunmoor park ny 10352
Email- velmarllc@tridomail.Com
Company phone number 555-318-6094
Cell number- 555-742-0583
Web site - velmarllc.Com
My name Gerald tomasino

Target Market(s)

Construction , home improvement, remodeling

Industry/Entity Type

Construction

Contact Information for Business Card

It has to be moder but at the same time simple

Font styles to use
Sans Serif

Colors
0255a3
ffffff
000000
f78f20
b1b1b1
9d9d9d
1b1b1b
33a6d7
ec1f27

Requirements
Must have
• My logo on one side maybe with a some kind of background on the other side all my information
Nice to have
• Some kind of background pictures provided by you .PLEASE HAVE ACCOUNT WITH PIXELVAULT WILL NOT PAY ANY EXTRA FEES .
Should not have
• Any kind of hamer, nails,screws, helmets itp. Please do not copy the other designs come up with something new.

```html
<!DOCTYPE html>
<html lang="en">
<head>
<meta charset="utf-8">
<title>Velmar Construction LLC – Business Card</title>
<link href="https://fonts.googleapis.com/css2?family=Arimo:wght@400;700&display=swap" rel="stylesheet">
<style>
  :root {
    --stage: #3d4656;
    --paper: #ffffff;
    --ink: #000000;
    --ink-soft: #1b1b1b;
    --band-sub: #b1b1b1;
    --brand-blue: #0255a3;
    --sky-top: #f4f7fb;
    --sky-bottom: #dfe6ef;
    --tower-light: #c9d2de;
    --tower-dark: #4a5466;
  }
  * { box-sizing: border-box; margin: 0; padding: 0; }
  html, body {
    width: 1200px;
    height: 800px;
    overflow: hidden;
  }
  body {
    background: var(--stage);
    font-family: "Arimo", Arial, sans-serif;
    display: flex;
    align-items: center;
    justify-content: center;
    gap: 60px;
  }
  .card {
    position: relative;
    width: 520px;
    height: 297px;
    background: var(--paper);
    box-shadow: 0 6px 18px rgba(0, 0, 0, 0.35);
    overflow: hidden;
  }

  /* Information side */
  .title-band {
    position: absolute;
    top: 30px;
    right: 0;
    width: 280px;
    height: 52px;
    background: var(--ink);
    color: var(--paper);
    text-align: right;
    padding: 10px 18px 0 0;
  }
  .title-band .company {
    font-weight: 700;
    font-size: 15px;
    letter-spacing: 0.3px;
  }
  .title-band .person {
    font-size: 12.5px;
    color: var(--band-sub);
    margin-top: 3px;
  }
  .contact {
    position: absolute;
    left: 34px;
    bottom: 28px;
    list-style: none;
    color: var(--ink-soft);
    font-weight: 700;
    font-size: 12.5px;
    line-height: 1.3;
  }
  .contact .gap { margin-top: 12px; }

  /* Logo side */
  .logo-side {
    background: linear-gradient(180deg, var(--sky-top), var(--sky-bottom));
  }
  .brand {
    position: absolute;
    top: 36px;
    right: 30px;
    display: flex;
    align-items: center;
    gap: 12px;
  }
  .brand .mark {
    width: 26px;
    height: 26px;
    background: var(--brand-blue);
  }
  .brand .name {
    font-weight: 700;
    font-size: 22px;
    color: var(--ink-soft);
    letter-spacing: 0.5px;
  }
  .backdrop {
    position: absolute;
    left: 0;
    right: 0;
    bottom: 0;
    height: 160px;
    background: linear-gradient(180deg, var(--tower-light) 0%, #8893a4 45%, var(--tower-dark) 100%);
  }
</style>
</head>
<body>
  <section class="card info-side" aria-label="Business card, information side">
    <div class="title-band">
      <p class="company">VELMAR CONSTRUCTION LLC</p>
      <p class="person">Gerald Tomasino</p>
    </div>
    <ul class="contact">
      <li>Cell : 555-742-0583</li>
      <li>Phone : 555-318-6094</li>
      <li class="gap">Email : velmarllc@tridomail.Com</li>
      <li>Website : www.velmarllc.Com</li>
      <li>Address : 418 Harbor 87th. Dunmoor Park NY 10352</li>
    </ul>
  </section>

  <section class="card logo-side" aria-label="Business card, logo side">
    <div class="brand">
      <span class="mark"></span>
      <span class="name">VELMAR CONSTRUCTION LLC</span>
    </div>
    <div class="backdrop" role="img" aria-label="Photograph of a modern glass and steel building facade against a pale sky"></div>
  </section>
</body>
</html>
```